Upmarket designer fashion & gift boutique card design

I need a business card that captures the vision of my customer & store. I am a ladies fashion boutique in the beautiful Northern Beaches of Sydney. I stock top australian designer fashion that is bold, colourful, & eccentric. My store also carries quirky & retro gift ware & unique statement jewellery. I want a card that is as colourful & eccentric as the designers I stock & the customer I attract. I love bold bright colours, leopard print, abstract or geometric shapes but nothing to fluffy or girly. I have attached my logo which is to be included on one side of the card.

Target Market(s)

25+ with a strong focus on the fabulous 30's & 40's

Industry/Entity Type

Boutique

Contact Information for Business Card

Delia Marchbank, Director, Shop 5/17 Wattlecrest Lane Coralvale NSW 2196, delia@tulvatulva.com.au ABN 61 307 594 218, mobile number 0482 716 053 www.facebook.com/tulvatulva

Font styles to use
Sans Serif

Colors

Designer to choose colors to be used in the design.

Requirements
Must have
• Open mind- although leopard or zebra print would win some votes
Nice to have
• Unique, fun,bold, quirky & different - hit me with your best shot!
Should not have
• No swirly/running writing text please

```html
<!DOCTYPE html>
<html lang="en">
<head>
<meta charset="utf-8">
<title>tulva tulva – Business Card</title>
<link rel="stylesheet" href="https://fonts.googleapis.com/css2?family=Josefin+Sans:wght@300;400;600&display=swap">
<style>
  :root {
    --royal-blue: #1d4f95;
    --deep-blue: #163f7c;
    --gold: #c9953a;
    --gold-light: #f1d27a;
    --gold-dark: #9c6a22;
    --cream: #f6f0e0;
    --cream-shade: #e6dcc4;
    --ink: #2a2622;
    --logo-teal: #2f8f9a;
    --page: #ffffff;
  }
  * { box-sizing: border-box; margin: 0; padding: 0; }
  html, body {
    width: 886px;
    height: 1200px;
    overflow: hidden;
    background: var(--page);
    font-family: "Josefin Sans", sans-serif;
  }
  .card {
    position: absolute;
    left: 0;
    width: 886px;
    background: linear-gradient(135deg, var(--gold-light), var(--gold) 40%, var(--gold-dark) 70%, var(--gold-light));
    padding: 14px;
  }
  .card--front { top: 0; height: 573px; }
  .card--back { top: 621px; height: 579px; }
  .card__surface {
    position: relative;
    width: 100%;
    height: 100%;
    overflow: hidden;
  }
  .damask-field {
    position: absolute;
    inset: 0;
    background:
      radial-gradient(ellipse at 20% 25%, rgba(214,160,70,0.45), transparent 30%),
      radial-gradient(ellipse at 60% 20%, rgba(214,160,70,0.4), transparent 28%),
      radial-gradient(ellipse at 90% 30%, rgba(214,160,70,0.4), transparent 26%),
      radial-gradient(ellipse at 35% 85%, rgba(214,160,70,0.4), transparent 28%),
      radial-gradient(ellipse at 80% 85%, rgba(214,160,70,0.4), transparent 28%),
      linear-gradient(180deg, var(--royal-blue), var(--deep-blue));
  }
  .torn-band {
    position: absolute;
    left: 0;
    width: 100%;
  }
  .card--front .torn-band { top: 233px; height: 208px; }
  .card--back .torn-band { top: 150px; height: 292px; }
  .torn-band svg { position: absolute; inset: 0; width: 100%; height: 100%; }
  .band-content {
    position: absolute;
    inset: 0;
    display: flex;
    flex-direction: column;
    align-items: center;
    justify-content: center;
  }
  .brand-name {
    font-weight: 600;
    font-size: 86px;
    letter-spacing: 1px;
    color: var(--logo-teal);
    line-height: 1;
    margin-left: 16px;
  }
  .brand-tagline {
    align-self: flex-end;
    margin-right: 218px;
    margin-top: 6px;
    font-weight: 400;
    font-size: 21px;
    color: var(--ink);
    letter-spacing: 0.5px;
  }
  .contact-details {
    list-style: none;
    text-align: center;
    color: var(--ink);
    font-weight: 300;
    font-size: 24px;
    letter-spacing: 1.5px;
    line-height: 30.5px;
    margin-top: 8px;
  }
  .contact-details .small { font-size: 21px; }
</style>
</head>
<body>

<section class="card card--front">
  <div class="card__surface">
    <div class="damask-field" role="img" aria-label="Gold damask pattern on royal blue"></div>
    <div class="torn-band">
      <svg viewBox="0 0 100 100" preserveAspectRatio="none" aria-hidden="true">
        <polygon fill="var(--cream-shade)" points="0,6 8,3 15,8 22,2 30,7 38,3 46,9 54,4 62,8 70,2 78,7 86,3 93,8 100,4 100,96 92,93 84,98 76,94 68,99 60,95 52,98 44,93 36,98 28,94 20,99 12,95 5,98 0,94"/>
        <polygon fill="var(--cream)" points="0,10 7,6 14,11 23,5 31,10 39,6 47,12 55,7 63,11 71,5 79,10 87,6 94,11 100,8 100,91 93,89 85,94 77,90 69,95 61,91 53,94 45,89 37,94 29,90 21,95 13,91 6,94 0,90"/>
      </svg>
      <div class="band-content">
        <div class="brand-name">tulva tulva</div>
        <div class="brand-tagline">Gift and Fashion</div>
      </div>
    </div>
  </div>
</section>

<section class="card card--back">
  <div class="card__surface">
    <div class="damask-field" role="img" aria-label="Gold damask pattern on royal blue"></div>
    <div class="torn-band">
      <svg viewBox="0 0 100 100" preserveAspectRatio="none" aria-hidden="true">
        <polygon fill="var(--cream-shade)" points="0,4 8,2 15,6 22,1 30,5 38,2 46,7 54,3 62,6 70,1 78,5 86,2 93,6 100,3 100,97 92,95 84,99 76,96 68,99 60,96 52,99 44,95 36,99 28,96 20,99 12,96 5,99 0,96"/>
        <polygon fill="var(--cream)" points="0,8 7,5 14,9 23,4 31,8 39,5 47,10 55,6 63,9 71,4 79,8 87,5 94,9 100,7 100,93 93,92 85,96 77,93 69,96 61,93 53,96 45,92 37,96 29,93 21,96 13,93 6,96 0,92"/>
      </svg>
      <div class="band-content">
        <ul class="contact-details">
          <li>Delia Marchbank, Director,</li>
          <li>Shop 5/17 Wattlecrest Lane</li>
          <li>Coralvale NSW 2196,</li>
          <li class="small">delia@tulvatulva.com.au</li>
          <li>ABN 61 307 594 218,</li>
          <li class="small">mobile number 0482 716 053</li>
          <li class="small">www.facebook.com/tulvatulva</li>
        </ul>
      </div>
    </div>
  </div>
</section>

</body>
</html>
```